TOBREL Business Card Design

We need a business card design for a current Plastering company now moving to building and constructing new homes.
We have been in the Plastering(rendering) business for 15yrs and have made a good name with our customers for our Top Quality of work that we provide.
We would like TOBREL to be the main attraction with an image of architectural roof tops or house design within it. Blue Yellow and Black are colours we like but are willing to see other ideas.
We would like the design to be modern and communicate quality and experience.
Industry/Entity Type
Building
Contact Information for Business Card
TOBREL Building and Plastering
PO BOX 73519 Casuarina Darwin NT 0812
PH/Fax: 08 83170925 Email: tobrel@wavemail.example
Glen: 0419372654 Ruth:0408631597
ABN:57 208 931 446

```html
<!DOCTYPE html>
<html lang="en">
<head>
<meta charset="utf-8">
<title>TOBREL Building and Plastering – Business Card</title>
<link rel="stylesheet" href="https://fonts.googleapis.com/css2?family=Roboto+Condensed:wght@400;500&display=swap">
<style>
  :root {
    --page: #ffffff;
    --card: #121212;
    --tone-mid: #3e4443;
    --tone-light: #6f7877;
    --text: #ffffff;
  }
  * { margin: 0; padding: 0; box-sizing: border-box; }
  html, body {
    width: 1200px;
    height: 741px;
    overflow: hidden;
    background: var(--page);
  }
  .card {
    position: absolute;
    left: 46px;
    top: 46px;
    width: 1106px;
    height: 646px;
    background: var(--card);
    overflow: hidden;
    font-family: "Roboto Condensed", "Arial Narrow", sans-serif;
    color: var(--text);
  }
  .backdrop {
    position: absolute;
    inset: 0;
    background: linear-gradient(135deg,
      var(--card) 0%,
      var(--card) 30%,
      var(--tone-mid) 62%,
      var(--tone-light) 100%);
  }
  .brand {
    position: absolute;
    left: 26px;
    top: 30px;
    width: 300px;
  }
  .brand-name {
    font-weight: 400;
    font-size: 78px;
    line-height: 1;
    letter-spacing: 6px;
    white-space: nowrap;
  }
  .brand-tagline {
    margin-top: 6px;
    font-weight: 400;
    font-size: 18px;
    letter-spacing: 2.4px;
    white-space: nowrap;
  }
  .contact {
    position: absolute;
    right: 43px;
    top: 438px;
    text-align: right;
    font-weight: 500;
    font-size: 29px;
    line-height: 37.8px;
    white-space: nowrap;
  }
</style>
</head>
<body>
  <div class="card">
    <div class="backdrop" role="img" aria-label="Decorative translucent grey diagonal light bands on black"></div>

    <div class="brand">
      <div class="brand-name">TOBREL</div>
      <div class="brand-tagline">Building and Plastering</div>
    </div>

    <div class="contact">
      <p class="contact-company">TOBREL Building and Plastering</p>
      <p class="contact-address">PO BOX 73519 Casuarina Darwin NT 0812</p>
      <p class="contact-office">PH/Fax: 08 83170925 Email: tobrel@wavemail.example</p>
      <p class="contact-people">Glen: 0419372654 Ruth:0408631597</p>
      <p class="contact-abn">ABN:57 208 931 446</p>
    </div>
  </div>
</body>
</html>
```